Visit card for Luxury Alpine home

Velvet Ridge Chalet (Hinterthal, Austria) – visit card

Brief: To design a visit card (4/4) that can be both left for existing guests and handed out to friends/business contacts to promote our luxury holiday home in the Austrian alps which can be rented year -round but primarily for summer (hiking/biking/golf) and winter (skiing). Primary focus is for family as its a 3br/3ba place that is usually booked for either a larger family or two families.

Basic information required/purpose: email/contact info. Basic information about the place, location, possibly some ideas/icons about what to do. Imagery that gives people the idea about luxury/fun/mountains etc. Hopefully the card would be something to interest them enough to check out the website and eventually make a direct booking with us.

Our details and photos:

https://velvetridgechalet.com
https://www.facebook.com/velvetridgechalet/

contact information for people to book:
stay.brenvale@larkpost.net
+420 604918352

some other resources:

http://www.tamrisberg-info.at/en/vacation.html
the moutains are called Hochkoenig and our village is Hinterthal which is next to Maria alm

Target Market(s)

European (winter) and Middle-Eastern (summer) families.

Industry/Entity Type

Travel

Contact Information for Business Card

standard 4/4 to be used for prospect

Font styles to use
Sans Serif

Colors

Designer to choose colors to be used in the design.

Requirements
Must have
• all relevant information for the client to contact us
• colorful/luxury imagery of the property (we can provide better photo quality that the web downloads)
Nice to have
• not particular about fonts. preferring subdued colours

```html
<!DOCTYPE html>
<html lang="en">
<head>
<meta charset="utf-8">
<title>Velvet Ridge Chalet – Booking Card</title>
<link href="https://fonts.googleapis.com/css2?family=Cabin+Condensed:wght@400;600;700&display=swap" rel="stylesheet">
<style>
  :root {
    --wood-light: #f1e9e1;
    --wood-mid: #e6dbd0;
    --ink: #111111;
    --white: #ffffff;
    --amber: #d4862f;
    --rust: #c55e27;
    --cocoa: #6a463b;
    --snow-sky: #6f9ad0;
    --snow: #e9eef4;
    --timber: #b98a5c;
    --interior-warm: #c9a27a;
    --interior-stone: #7a6a5a;
    --bed-wine: #6e1e22;
    --bed-linen: #f2f0ee;
  }
  * { margin: 0; padding: 0; box-sizing: border-box; }
  html, body {
    width: 1200px; height: 750px; overflow: hidden;
    background: #ffffff;
  }
  .card {
    position: relative;
    width: 1200px; height: 750px;
    background: linear-gradient(180deg, var(--wood-light) 0%, var(--wood-mid) 50%, var(--wood-light) 100%);
    font-family: "Cabin Condensed", "Arial Narrow", sans-serif;
    overflow: hidden;
  }
  .photo {
    position: absolute; top: 38px; height: 268px;
  }
  .photo--exterior {
    left: 37px; width: 375px;
    background: linear-gradient(180deg, var(--snow-sky) 0%, #a7c0df 45%, var(--timber) 62%, var(--snow) 80%, #ffffff 100%);
  }
  .photo--living {
    left: 414px; width: 374px;
    background: linear-gradient(160deg, var(--interior-stone) 0%, var(--interior-warm) 45%, #e4c9a4 100%);
  }
  .photo--bedroom {
    left: 790px; width: 372px;
    background: linear-gradient(100deg, #2a2826 0%, #2a2826 25%, var(--bed-wine) 40%, var(--bed-linen) 70%, #ffffff 100%);
  }
  .headline {
    position: absolute; top: 316px; left: 0; width: 1200px;
    text-align: center;
    font-weight: 700; font-size: 39px; letter-spacing: 4px; word-spacing: 6px;
    color: var(--ink);
  }
  .contact {
    position: absolute; top: 371px; height: 344px;
    display: flex; flex-direction: column; align-items: center;
    color: var(--white);
  }
  .contact--phone { left: 34px; width: 377px; background: var(--amber); }
  .contact--email { left: 411px; width: 377px; background: var(--rust); }
  .contact--web { left: 789px; width: 373px; height: 341px; background: var(--cocoa); }
  .contact__icon { margin-top: 51px; width: 98px; height: 98px; }
  .contact__text {
    margin-top: 40px;
    font-size: 35px; font-weight: 400; letter-spacing: 0.3px;
    color: var(--white); text-decoration: none; white-space: nowrap;
  }
  .contact--web .contact__icon { margin-top: 50px; }
  .contact--web .contact__text { margin-top: 38px; }
</style>
</head>
<body>
<main class="card">
  <div class="photo photo--exterior" role="img" aria-label="Photo of the timber chalet exterior in deep snow under a blue sky"></div>
  <div class="photo photo--living" role="img" aria-label="Photo of the open living and dining room with stone fireplace and wooden beams"></div>
  <div class="photo photo--bedroom" role="img" aria-label="Photo of a bed with white pillows against a deep red headboard"></div>

  <h1 class="headline">To Book Please Contact Us</h1>

  <section class="contact contact--phone">
    <svg class="contact__icon" viewBox="0 0 100 100" aria-hidden="true">
      <circle cx="50" cy="50" r="45" fill="none" stroke="#111" stroke-width="5"/>
      <path d="M33 27c3-3 7-3 9 0l5 8c2 3 1 6-1 8l-3 3c2 6 8 12 14 14l3-3c2-2 5-3 8-1l8 5c3 2 3 6 0 9l-4 4c-4 4-12 3-22-5-9-7-17-16-21-26-3-8-2-13 1-16z" fill="#111"/>
    </svg>
    <a class="contact__text" href="tel:+420604918352">+420 - 604918352</a>
  </section>

  <section class="contact contact--email">
    <svg class="contact__icon" viewBox="0 0 100 100" aria-hidden="true">
      <circle cx="50" cy="50" r="49" fill="#111"/>
      <rect x="42" y="33" width="40" height="30" fill="#fff"/>
      <path d="M42 33l20 17 20-17" fill="none" stroke="#111" stroke-width="3"/>
      <rect x="14" y="37" width="22" height="4" fill="#fff"/>
      <rect x="18" y="46" width="18" height="4" fill="#fff"/>
      <rect x="22" y="55" width="14" height="4" fill="#fff"/>
    </svg>
    <a class="contact__text" href="mailto:stay.brenvale@larkpost.net">stay.brenvale@larkpost.net</a>
  </section>

  <section class="contact contact--web">
    <svg class="contact__icon" viewBox="0 0 100 100" aria-hidden="true">
      <circle cx="50" cy="50" r="49" fill="#111"/>
      <text x="50" y="57" text-anchor="middle" font-family="Arial, sans-serif" font-weight="700" font-size="22" fill="#fff">www</text>
      <path d="M62 62l0 20 5-5 5 8 4-2-5-8 7-1z" fill="#fff"/>
    </svg>
    <a class="contact__text" href="https://velvetridgechalet.com">velvetridgechalet.com</a>
  </section>
</main>
</body>
</html>
```